Tallowmoor Letterheads Design

Hello, we have just upgraded this project for a guaranteed payment.

We are currently going through a re-branding exercise internally. Our logo is attached as a PDF file.

We are happy with our logo but would like to investigate how we can best apply the logo to our letterheads and compliment slips.

We are a quality printing company in England. Despite our name we are very professional and offer a personal service.

Our new website is under construction and here is a link to show you how it looks: http://brackenpress.v4ntor.co.uk

The style must be professional and steer away from "tacky" otherwise it makes our company look very low budget and just a bit silly.

We would like to see elements of creativity though, so please, nothing too boring.

I have attached our new logo, there is an option for use on white or black.

Cheers
Tallowmoor Team

Reason: We have increased the deadline due to an internal delay to things, we now have more time before we need anything to be printed.

Industry/Entity Type

Construction

Requirements
Must have
• IMPORTANT! Please do not tweak or change our logo in any way. A few designs show vast changes in the logo, this is not what we require. Please do not change the logo in any way. Thanks
Nice to have
• Classy but approachable. Elements of "quirky" would be nice to see.
Should not have
• A Tacky feel

```html
<!DOCTYPE html>
<html lang="en">
<head>
<meta charset="utf-8">
<title>Tallowmoor Letterhead</title>
<link rel="stylesheet" href="https://fonts.googleapis.com/css2?family=Source+Sans+3:wght@400;600;700&display=swap">
<style>
  :root {
    --paper: #ffffff;
    --ink: #6d6e71;
    --panel: #231f20;
    --accent: #e4097a;
    --panel-text: #ffffff;
    --signature: #d9d9db;
  }
  * { box-sizing: border-box; margin: 0; padding: 0; }
  html, body { width: 927px; height: 1200px; overflow: hidden; background: var(--paper); }
  .letterhead {
    position: relative;
    width: 927px;
    height: 1200px;
    background: var(--paper);
    font-family: "Source Sans 3", Arial, sans-serif;
    color: var(--ink);
  }
  .accent-stripe {
    position: absolute; left: 672px; top: 0; width: 7px; height: 1200px;
    background: var(--accent);
  }
  .side-panel {
    position: absolute; left: 685px; top: 0; width: 242px; height: 1200px;
    background: var(--panel);
  }
  .letter {
    position: absolute; left: 49px; top: 194px; width: 578px;
    font-size: 15.8px; line-height: 28.7px;
  }
  .letter .salutation { margin-bottom: 21px; }
  .letter .body { text-align: justify; }
  .sign-off {
    position: absolute; left: 49px; top: 840px;
    font-size: 15.8px;
  }
  .signature {
    position: absolute; left: 47px; top: 874px; width: 66px; height: 46px;
    background: var(--signature); border-radius: 4px;
  }
  .brand {
    position: absolute; left: 685px; top: 600px; width: 242px;
    text-align: center; color: var(--panel-text);
  }
  .brand .mark {
    width: 14px; height: 14px; border-radius: 50%;
    background: var(--accent); margin: 0 auto 12px;
  }
  .brand .name {
    font-weight: 700; font-size: 29px; line-height: 1;
  }
  .brand .tagline {
    font-size: 12.5px; margin-top: 3px;
  }
  .contact {
    position: absolute; left: 685px; top: 1074px; width: 242px;
    text-align: center; color: var(--panel-text);
    font-size: 13px; line-height: 18.6px;
  }
  .contact .email { color: var(--accent); }
</style>
</head>
<body>
<div class="letterhead">
  <div class="letter">
    <p class="salutation">Dear Sir,</p>
    <p class="body">Lorem ipsum dolor sit amet, consectetuer adipiscing elit. Aenean commodo ligula eget dolor. Aenean massa. Cum sociis natoque penatibus et magnis dis parturient montes, nascetur ridiculus mus. Donec quam felis, ultricies nec, pellentesque eu, pretium quis, sem. Nulla consequat massa quis enim. Donec pede justo, fringilla vel, aliquet nec, vulputate eget, arcu. In enim justo, rhoncus ut, imperdiet a, venenatis vitae, justo. Nullam dictum felis eu pede mollis pretium. Integer tincidunt. Cras dapibus. Vivamus elementum semper nisi. Aenean vulputate eleifend tellus. Aenean leo ligula, porttitor eu, consequat vitae, eleifend ac, enim. Aliquam lorem ante, dapibus in, viverra quis, feugiat a, tellus. Phasellus viverra nulla ut metus varius laoreet. Quisque rutrum. Aenean imperdiet. Etiam ultricies nisi vel augue. Curabitur ullamcorper ultricies nisi. Nam eget dui. Etiam rhoncus. Maecenas tempus, tellus eget condimentum rhoncus, sem quam semper libero, sit amet adipiscing sem neque sed ipsum. Nam quam nunc, blandit vel, luctus pulvinar, hendrerit id, lorem.</p>
  </div>

  <p class="sign-off">From</p>
  <div class="signature" role="img" aria-label="Handwritten signature of the sender"></div>

  <div class="accent-stripe"></div>
  <div class="side-panel"></div>

  <div class="brand">
    <div class="mark"></div>
    <div class="name">Tallowmoor</div>
    <div class="tagline">Quality Printing</div>
  </div>

  <div class="contact">
    <p>T : 0208 555 0173</p>
    <p>E : <span class="email">sales@tallowmoor.co.uk</span></p>
    <p>Address : 12 Mill Lane,</p>
    <p>Ashcombe-On-The-Green,</p>
    <p>Ashcombe, Surrey, AB1 2CD</p>
  </div>
</div>
</body>
</html>
```